Label Design for a sexy ladies 5 pocket skinny

We need modern packaging design for women's skinny 5 pocket pants for a brand name Quill. All kinds of packaging designs are welcome.
The pant is folded and packaged in a poly bag. We require a label design for the brand name Quill. The main label will be attached by a string on the belt loop. the size of that label will 25cm in length and 10cm wide. This is the first label the customer see's when she picks up the garment. Therefore, we require an eye catching design for that. If required it could have certain information about the pant on the main label such as Comfort fit, Wrinkle-resistant, machine washable, luxury fabric. But, if you feel that adding the above information spoils the design of the label then it is not a must to include the above information. On the back of the label we like to include the information that this pant was manufactured in an Terravo Gold certified green plant and hence the damage to the environment because of the plant is nill.
The second label is attached on to the waist band and the purpose of that label is to include the size of the pant such 32x32. The size of that label is 8cm in length and 4cm in width. There is no design on the back on this label it has to be blank.
Sample is given for what we currently use for our mens chino pant. we are looking for something very different.
Reason: because there was a delay in the project being approved by pixel harbor.

```html
<!DOCTYPE html>
<html lang="en">
<head>
<meta charset="utf-8">
<title>Quill Women's Skinny Labels</title>
<link href="https://fonts.googleapis.com/css2?family=Righteous&family=Abril+Fatface&display=swap" rel="stylesheet">
<style>
  :root {
    --pink: #ff0a86;
    --teal: #00c0c8;
    --yellow: #f5c518;
    --ink: #111111;
    --white: #ffffff;
    --badge: #f9a6cf;
    --edge: #8a7a6a;
  }
  * { box-sizing: border-box; margin: 0; padding: 0; }
  html, body { width: 1200px; height: 926px; overflow: hidden; background: var(--white); }
  .canvas { position: relative; width: 1200px; height: 926px; }

  .label {
    position: absolute;
    overflow: hidden;
    border: 1px solid var(--edge);
    border-radius: 6px;
    box-shadow: 2px 3px 5px rgba(0,0,0,0.35);
    background: var(--teal);
  }
  .label-front { left: 273px; top: 77px; width: 246px; height: 733px; }
  .label-back  { left: 577px; top: 77px; width: 246px; height: 733px; }
  .label-size  { left: 869px; top: 244px; width: 208px; height: 411px; }

  .label-bands { position: absolute; inset: 0; width: 100%; height: 100%; }

  .art-swirls {
    position: absolute;
    z-index: 1;
    background:
      radial-gradient(circle at 35% 40%, rgba(17,17,17,0.85) 0 18%, transparent 19%),
      radial-gradient(circle at 70% 30%, rgba(17,17,17,0.8) 0 20%, transparent 21%),
      radial-gradient(circle at 55% 70%, rgba(17,17,17,0.75) 0 22%, transparent 23%),
      radial-gradient(ellipse at center, #8a1050 0%, #c80a6e 60%, rgba(255,10,134,0) 75%);
    border-radius: 46% 40% 48% 42%;
  }
  .label-front .art-swirls { left: 0; top: 14px; width: 246px; height: 380px; }
  .label-back .art-swirls  { left: 0; top: 30px; width: 246px; height: 260px; }

  .art-moose {
    position: absolute;
    z-index: 1;
    left: 0; width: 246px;
    background: linear-gradient(160deg, var(--yellow) 0%, #e8b414 45%, #3a2a10 75%, var(--pink) 100%);
    border-radius: 40% 45% 0 0;
  }
  .label-front .art-moose { top: 492px; height: 241px; }
  .label-back .art-moose  { top: 486px; height: 247px; }

  .tag, .features, .origin-note, .cert-badge { z-index: 2; }

  .tag {
    position: absolute;
    background: var(--yellow);
    border-radius: 30px;
    font-family: "Righteous", sans-serif;
    color: var(--ink);
    text-transform: uppercase;
    text-align: center;
    letter-spacing: 0.5px;
  }
  .label-front .tag { left: 10px; top: 94px; width: 232px; height: 56px; line-height: 56px; font-size: 20px; transform: rotate(-5deg); }
  .label-back .tag  { left: 26px; top: 292px; width: 194px; height: 44px; line-height: 44px; font-size: 15px; transform: rotate(-4deg); }

  .features {
    position: absolute;
    right: 18px; top: 398px;
    font-family: "Righteous", sans-serif;
    font-size: 17px; line-height: 21px;
    text-transform: uppercase;
    text-align: right;
    color: var(--ink);
    letter-spacing: 0.6px;
  }
  .origin-note {
    position: absolute;
    left: 0; width: 246px; top: 358px;
    font-family: "Righteous", sans-serif;
    font-size: 15px; line-height: 19.5px;
    text-transform: uppercase;
    text-align: center;
    color: var(--ink);
    letter-spacing: 0.4px;
  }
  .cert-badge {
    position: absolute;
    left: 64px; top: 46px;
    width: 100px; height: 100px;
    border-radius: 50%;
    background: var(--badge);
  }

  .size-stack {
    position: absolute;
    inset: 0;
    font-family: "Abril Fatface", serif;
    color: var(--ink);
    text-align: center;
  }
  .size-stack span {
    position: absolute;
    left: 0; width: 100%;
    text-shadow: -5px -3px 0 var(--yellow);
  }
  .size-num { font-size: 64px; line-height: 64px; }
  .size-word { font-size: 32px; line-height: 34px; }
  .size-x { font-size: 32px; line-height: 34px; }
</style>
</head>
<body>
<main class="canvas">

  <section class="label label-front" aria-label="Main label, front">
    <svg class="label-bands" viewBox="0 0 246 733" preserveAspectRatio="none" aria-hidden="true">
      <polygon points="50,0 246,0 246,380 220,733 0,733 0,470" fill="var(--white)"/>
      <polygon points="68,0 246,0 246,420 205,733 0,733 0,590" fill="var(--pink)"/>
    </svg>
    <div class="art-swirls" role="img" aria-label="Hand-drawn black contour swirl pattern"></div>
    <div class="tag">Women's Skinny</div>
    <p class="features">Comfort fit,<br>wrinkle resistant,<br>machine washable<br>luxury fabric</p>
    <div class="art-moose" role="img" aria-label="Sketched moose illustration on a yellow splash"></div>
  </section>

  <section class="label label-back" aria-label="Main label, back">
    <svg class="label-bands" viewBox="0 0 246 733" preserveAspectRatio="none" aria-hidden="true">
      <polygon points="40,0 246,0 246,230 190,733 0,733 0,500" fill="var(--white)"/>
      <polygon points="56,0 246,0 246,280 178,733 0,733 0,620" fill="var(--pink)"/>
    </svg>
    <div class="art-swirls" role="img" aria-label="Hand-drawn black and teal contour swirl pattern"></div>
    <div class="cert-badge" aria-hidden="true"></div>
    <div class="tag">Women's Skinny</div>
    <p class="origin-note">This Quill chino<br>was proudly produced<br>in a Terravo Gold<br>certified green plant<br>with no negative<br>enviromental impact</p>
    <div class="art-moose" role="img" aria-label="Sketched moose illustration on a yellow splash"></div>
  </section>

  <section class="label label-size" aria-label="Size label">
    <svg class="label-bands" viewBox="0 0 208 411" preserveAspectRatio="none" aria-hidden="true">
      <polygon points="0,0 208,0 208,411 0,411" fill="var(--yellow)"/>
      <polygon points="22,0 208,0 208,290 196,411 0,411 0,150" fill="var(--pink)"/>
    </svg>
    <div class="size-stack">
      <span class="size-num" style="top:62px">34</span>
      <span class="size-word" style="top:148px">Waist</span>
      <span class="size-x" style="top:196px">x</span>
      <span class="size-num" style="top:242px">36</span>
      <span class="size-word" style="top:326px">Length</span>
    </div>
  </section>

</main>
</body>
</html>
```